Geschäftspapiere für Ingenieurbüro gesucht
Zielgruppe
Name: Ingenieurbüro Raltke
Künstliche Intelligenz und Digitalisierung
Unser Schwerpunkt ist die Optimierung des Indoor-Anbaus teurer Pflanzen wie z.B. Cannabis:
- Beratung von Cannabis-Erzeugern
- Lieferung von Technologie (Hardware, Software)
- Langzeitbetreuung unserer Kunden
Zielgruppe:
Cannabis-Erzeuger
Details:
Ing.-Büro Raltke
Falkenhainweg 12
16552 Bornwalde bei Berlin * Germany
Tel.: 030/582914-71
Fax: 030/58291479
E-Mail: info@ing-büro-raltke.de
Web: www.ing-büro-raltke.de
Konto:
Kornbank Berlin
IBAN: DE27300200300918264405
BIC: KRBKDEHH
USt.-ID: DE51928374615
Aufgabenstellung
Modernes, sachliches, seriöses Design, Hauptfarbe: türkis.
Nichts Verspieltes.
Gerne kann eine stilisierte Cannabis-Blüte oder -pflanze vorkommen, muss aber nicht.

```html
<!DOCTYPE html>
<html lang="de">
<head>
<meta charset="utf-8">
<title>Briefbogen Ingenieurbüro Raltke</title>
<link href="https://fonts.googleapis.com/css2?family=Arimo&family=Carlito:wght@400;700&display=swap" rel="stylesheet">
<style>
  :root {
    --turquoise: #4cbcb6;
    --turquoise-faint: #eef8f7;
    --ink: #1a1a1a;
    --grey-text: #5a5a5a;
    --rule-grey: #c9c9c9;
    --backdrop: #ebebeb;
    --paper: #ffffff;
  }
  html, body { margin: 0; padding: 0; width: 1200px; height: 1200px; overflow: hidden; background: var(--backdrop); }
  .sheet {
    position: absolute; left: 211px; top: 51px; width: 775px; height: 1096px;
    background: var(--paper); overflow: hidden;
  }
  .sheet > * { position: absolute; margin: 0; }

  .watermark { left: 139px; top: 573px; width: 500px; height: 500px; }

  .brand-mark { left: 601px; top: 39px; width: 60px; height: 60px; }
  .brand-name {
    left: 531px; top: 122px; width: 200px; text-align: center;
    font-family: "Carlito", sans-serif; font-weight: 400; font-size: 15px;
    color: var(--turquoise); white-space: nowrap;
  }

  .sender-line {
    left: 92px; top: 191px; font-family: "Carlito", sans-serif; font-size: 8.2px;
    color: var(--grey-text); white-space: nowrap;
  }
  .sender-line b { font-weight: 700; }
  .sender-line .sep { color: var(--turquoise); padding: 0 3px; }

  .recipient {
    left: 92px; top: 227px; font-family: "Arimo", sans-serif; font-size: 14px;
    line-height: 18.2px; color: var(--ink); font-style: normal;
  }
  .recipient .city { display: block; margin-top: 18.2px; }

  .info-column {
    left: 548px; top: 188px; height: 192px; border-left: 1px solid var(--rule-grey);
    padding-left: 8px; padding-top: 3px; font-family: "Carlito", sans-serif; font-size: 9px;
    line-height: 13.75px; color: var(--grey-text);
  }
  .info-column p { margin: 0 0 12px; }
  .info-column b { font-weight: 700; }
  .contact { display: flex; align-items: center; }
  .contact svg { width: 9px; height: 9px; margin-right: 9px; flex: none; }

  .fold-mark { left: 19px; width: 29px; height: 0; border-top: 1px solid var(--turquoise); }
  .fold-1 { top: 387px; } .fold-2 { top: 548px; } .fold-3 { top: 775px; }

  .letter {
    font-family: "Arimo", sans-serif; font-size: 14px; line-height: 19.4px; color: var(--ink);
    left: 92px; width: 620px;
  }
  .subject { top: 399px; }
  .body { top: 438px; }
  .body p { text-align: justify; margin: 0 0 19.4px; }
  .closing { top: 809px; }
</style>
</head>
<body>
<main class="sheet">
  <svg class="watermark" viewBox="0 0 100 100" aria-hidden="true">
    <circle cx="50" cy="50" r="46" fill="none" stroke="var(--turquoise-faint)" stroke-width="3.5"/>
  </svg>

  <svg class="brand-mark" viewBox="0 0 60 60" aria-hidden="true">
    <circle cx="30" cy="30" r="26" fill="none" stroke="var(--turquoise)" stroke-width="3"/>
  </svg>
  <p class="brand-name">Ingenieurbüro Raltke</p>

  <p class="sender-line"><b>Ing.-Büro Raltke</b><span class="sep">|</span>Falkenhainweg 12<span class="sep">|</span>16552 Bornwalde bei Berlin</p>

  <address class="recipient">
    Herrn<br>Max Mustermann<br>Musterstraße 00
    <span class="city">01234 Musterstadt</span>
  </address>

  <aside class="info-column">
    <p><b>Ing.-Büro Raltke</b><br>Falkenhainweg 12<br>16552 Bornwalde bei Berlin<br>Germany</p>
    <p>
      <span class="contact"><svg viewBox="0 0 10 10"><path d="M2 1 L4 3 L3 4 Q4.5 6 6 7 L7 6 L9 8 L8 9 Q3 8 1 2 Z" fill="none" stroke="var(--turquoise)" stroke-width="0.9"/></svg>030 582914-71</span>
      <span class="contact"><svg viewBox="0 0 10 10"><rect x="1" y="4" width="8" height="4" rx="1" fill="none" stroke="var(--turquoise)" stroke-width="0.9"/><rect x="3" y="1.5" width="4" height="2.5" fill="none" stroke="var(--turquoise)" stroke-width="0.9"/></svg>030 582914-79</span>
      <span class="contact"><svg viewBox="0 0 10 10"><rect x="1" y="2.5" width="8" height="5.5" fill="none" stroke="var(--turquoise)" stroke-width="0.9"/><path d="M1 2.5 L5 6 L9 2.5" fill="none" stroke="var(--turquoise)" stroke-width="0.9"/></svg>info@ing-büro-raltke.de</span>
      <span class="contact"><svg viewBox="0 0 10 10"><circle cx="5" cy="5" r="4" fill="none" stroke="var(--turquoise)" stroke-width="0.9"/><ellipse cx="5" cy="5" rx="1.8" ry="4" fill="none" stroke="var(--turquoise)" stroke-width="0.7"/><path d="M1 5 H9" stroke="var(--turquoise)" stroke-width="0.7"/></svg>www.ing-büro-raltke.de</span>
    </p>
    <p>Kornbank Berlin<br>IBAN: DE27 3002 0030 0918 2644 05<br>BIC: KRBKDEHH<br>USt.-ID: DE51928374615</p>
  </aside>

  <span class="fold-mark fold-1"></span>
  <span class="fold-mark fold-2"></span>
  <span class="fold-mark fold-3"></span>

  <p class="letter subject">Dies ist eine Betreffzeile</p>

  <div class="letter body">
    <p>Sehr geehrter Herr Mustermann, jeder Setzer hat für diesen Zweck immer etwas Blindtext parat. Blindtext ist im Umfang von einigen tausend Anschlägen, der für die »äußerliche« Gestaltung einer Publikation verwendet und dessen Inhalt unwichtig ist. Man setzt ihn oft zum Beispiel in verschiedenen Schriften und Schriftgrößen, um anderen zu zeigen, wie eine bestimmte Schrift wirkt.</p>
    <p>Oder man montiert auch komplette ganze Seiten mit sinnlosen Streifen von Blindtext, um das spätere Aussehen der Seiten zu simulieren. Man setzt ihn oft zum Beispiel in verschiedenen Schriften und Schriftgrößen, um anderen zu zeigen, wie eine bestimmte Schrift wirkt. Blindtext wird allerdings oft nur für die Teile einer Seite verwendet, die in so kleiner Schrift gesetzt werden, dass sie beim »Überfliegen« ungelesen bleiben.</p>
    <p>Jeder Setzer hat für diesen Zweck immer etwas Blindtext parat. Blindtext ist Umfang von einigen tausend Anschlägen, der für die »äußerliche« Gestaltung einer Publikation verwendet und dessen Inhalt unwichtig ist.</p>
  </div>

  <p class="letter closing">Mit freundlichen Grüßen</p>
</main>
</body>
</html>
```